Propose a revamped landing page

One template we like eg is https://www.tornavo.com but but cluttered Our logo and colors are attached to our logo and colors are printed on a white background what we have. So font usage ...
Number of Pages Required
1 page

```html
<!DOCTYPE html>
<html lang="en">
<head>
<meta charset="utf-8">
<title>Energy Ace – Always switch to the cheapest energy provider</title>
<link href="https://fonts.googleapis.com/css2?family=Cinzel:wght@400;700&family=Raleway:wght@400;500;700;800&display=swap" rel="stylesheet">
<style>
:root{
  --orange:#f5a623;
  --orange-light:#fbbf2a;
  --orange-deep:#f39c1a;
  --ember:#c2410c;
  --ink:#3d4248;
  --text:#4a4a4a;
  --muted:#666;
  --rule:#d9d9d9;
  --white:#fff;
  --footer:#f4f4f4;
  --night:#2c3138;
}
*{box-sizing:border-box;margin:0;padding:0}
html,body{width:1200px;height:2679px;overflow:hidden}
body{font-family:"Raleway",sans-serif;color:var(--text);background:var(--white);position:relative}
section,header,footer{position:absolute;left:0;width:1200px}
.heading{font-family:"Cinzel",serif;font-weight:400;text-transform:uppercase;letter-spacing:4px;text-align:center;position:absolute;left:0;width:1200px}
.accent{color:var(--orange)}
.divider{position:absolute;left:482px;width:236px;height:2px;background:var(--rule)}
.divider::after{content:"";position:absolute;left:93px;width:54px;height:3px;top:-1px;background:var(--orange)}
.btn{position:absolute;left:513px;width:175px;height:43px;border:1.5px solid var(--white);color:var(--white);font-size:14px;display:flex;align-items:center;justify-content:center;text-decoration:none}

/* header */
.site-header{top:0;height:102px;background:var(--white);box-shadow:0 2px 6px rgba(0,0,0,.12);z-index:2}
.brand{position:absolute;display:flex;align-items:center;gap:8px;font-family:"Raleway",sans-serif;font-weight:800;color:var(--orange)}
.site-header .brand{left:86px;top:26px;font-size:36px}
.brand-dot{width:18px;height:18px;border-radius:50%;background:var(--orange)}
.main-nav{position:absolute;left:352px;top:40px;display:flex;font-size:15px;color:var(--ink)}
.main-nav a{color:inherit;text-decoration:none;padding:0 22px;border-left:1px solid var(--rule)}
.main-nav a:first-child{border-left:none;padding-left:0}
.main-nav a:last-child{padding-right:0}

/* hero */
.hero{top:102px;height:511px;background:radial-gradient(ellipse at 30% 20%,var(--orange-light),var(--orange-deep) 75%)}
.hero-kicker{top:74px;font-size:30px;color:var(--white);letter-spacing:6px}
.hero-title{top:92px;font-size:230px;color:var(--ember);letter-spacing:70px;padding-left:70px;line-height:1.05}
.hero-tagline{position:absolute;top:343px;left:0;width:1200px;text-align:center;color:#5a3a05;font-size:18px;letter-spacing:4.5px}
.hero .btn{top:403px}

/* intro */
.intro{top:613px;height:446px}
.intro h2{top:80px;font-size:43px;line-height:53px;color:var(--ink)}
.intro .divider{top:210px}
.intro-copy{position:absolute;top:240px;left:250px;width:700px;text-align:center;font-size:13.5px;line-height:21px;color:var(--muted)}
.intro-copy p{margin-bottom:21px}

/* power band */
.power-band{top:1059px;height:472px;background:linear-gradient(180deg,#3a4049 0%,#2a2f36 55%,#1f242a 100%)}
.power-band h2{left:173px;width:auto;text-align:left;top:183px;font-size:45px;line-height:53px;color:var(--white);letter-spacing:4px}
.savings{position:absolute;left:848px;top:180px;color:var(--white)}
.savings-label{font-size:23px;letter-spacing:2px}
.savings-amount{font-size:66px;font-weight:700;color:var(--orange);letter-spacing:5px;line-height:1}
.savings-amount sup{font-size:30px;vertical-align:top}

/* benefits */
.benefits{top:1531px;height:496px}
.benefits h2{top:80px;font-size:44px;color:var(--ink)}
.benefits .divider{top:153px}
.benefit{position:absolute;top:207px;width:300px;text-align:center}
.benefit-icon{width:96px;height:96px;margin:0 auto;border:1.5px solid var(--orange);border-radius:50%;display:flex;align-items:center;justify-content:center}
.benefit h3{font-family:"Cinzel",serif;font-weight:400;color:var(--orange);font-size:22px;letter-spacing:1.5px;margin-top:24px}
.benefit p{font-size:13.5px;line-height:21px;color:var(--muted);margin-top:12px}

/* steps */
.steps{top:2027px;height:533px;background:var(--orange)}
.steps h2{top:82px;font-size:42px;color:var(--white);letter-spacing:5px}
.steps .divider{top:155px;background:rgba(255,255,255,.55)}
.steps .divider::after{background:var(--ink)}
.step{position:absolute;top:216px;width:320px}
.step-marker{position:absolute;left:0;top:0}
.step h3{position:absolute;left:66px;top:30px;font-family:"Cinzel",serif;font-weight:400;color:var(--white);font-size:22px;line-height:26px;letter-spacing:1px;width:240px}
.step p{position:absolute;left:66px;width:210px;font-size:13.5px;line-height:21px;color:var(--ink)}
.steps .btn{top:404px}

/* footer */
.site-footer{top:2560px;height:119px;background:var(--footer)}
.site-footer .brand{left:86px;top:38px;font-size:30px}
.footer-nav{position:absolute;left:314px;top:53px;font-size:11px;color:var(--ink)}
.footer-nav a{color:inherit;text-decoration:none}
.footer-nav span{margin:0 4px}
.copyright{position:absolute;left:818px;top:53px;font-size:11px;color:var(--ink)}
.social{position:absolute;left:1100px;top:50px;width:16px;height:16px;border-radius:50%;background:#3b5998}
</style>
</head>
<body>

<header class="site-header">
  <div class="brand">Energy Ace<span class="brand-dot"></span></div>
  <nav class="main-nav">
    <a href="#">That's How It Works</a><a href="#">Prices</a><a href="#">Ask?</a><a href="#">About Us</a><a href="#">Operations</a><a href="#">Experience</a><a href="#">Press</a>
  </nav>
</header>

<section class="hero">
  <p class="heading hero-kicker">Energy</p>
  <h1 class="heading hero-title">Ace</h1>
  <p class="hero-tagline">Always automatically switch to the cheapest energy provider.</p>
  <a class="btn" href="#">Register Now</a>
</section>

<section class="intro">
  <h2 class="heading">Never pay too much for<br><span class="accent">Electricity</span> &amp; <span class="accent">Gas</span> again</h2>
  <div class="divider"></div>
  <div class="intro-copy">
    <p>Gone are the days of bad deals, tedious rate comparison and boring exchange forms.</p>
    <p>With the automatic change service for Energy Aces you will never again pay too much for electricity and gas. And that, without touching a finger. We fight for you through the tariff jungle.</p>
    <p>So save your hard earned money and become an <span class="accent">Energy Ace</span>.</p>
  </div>
</section>

<section class="power-band" role="img" aria-label="Wind turbines and solar panels under a dark evening sky">
  <h2 class="heading">The cheapest of<br>all super powers</h2>
  <div class="savings">
    <div class="savings-label">Savings up to:</div>
    <div class="savings-amount">€850<sup>*</sup></div>
  </div>
</section>

<section class="benefits">
  <h2 class="heading">Register once, always save</h2>
  <div class="divider"></div>
  <div class="benefit" style="left:98px">
    <div class="benefit-icon">
      <svg width="48" height="48" viewBox="0 0 48 48" fill="none" stroke="#999" stroke-width="1.5" stroke-linejoin="round"><path d="M4 22 44 6 34 42 22 28Z"/><path d="M44 6 22 28v12l6-8"/></svg>
    </div>
    <h3>Independently</h3>
    <p>We work only for you. In order to<br>remain independent.</p>
  </div>
  <div class="benefit" style="left:450px">
    <div class="benefit-icon">
      <svg width="50" height="50" viewBox="0 0 50 50" fill="none" stroke="#999" stroke-width="1.5"><circle cx="20" cy="20" r="9"/><circle cx="20" cy="20" r="3.5"/><path d="M20 6v5M20 29v5M6 20h5M29 20h5M10 10l3.5 3.5M26.5 26.5 30 30M10 30l3.5-3.5M26.5 13.5 30 10"/><circle cx="36" cy="36" r="6"/><circle cx="36" cy="36" r="2.2"/><path d="M36 26v3.5M36 42.5V46M26 36h3.5M42.5 36H46"/></svg>
    </div>
    <h3>Automatically</h3>
    <p>You sign up once and we'll do the rest.<br>All automatically.</p>
  </div>
  <div class="benefit" style="left:802px">
    <div class="benefit-icon">
      <svg width="48" height="48" viewBox="0 0 48 48" fill="none" stroke="#999" stroke-width="1.5" stroke-linejoin="round"><rect x="6" y="16" width="34" height="24" rx="3"/><path d="M12 16 30 7l5 9"/><rect x="30" y="24" width="12" height="8" rx="2"/><circle cx="35" cy="28" r="1.2"/></svg>
    </div>
    <h3>Fair</h3>
    <p>Energy Aces stays more in Börsel.<br>Despite service charge.</p>
  </div>
</section>

<section class="steps">
  <h2 class="heading">How do I become Energy Ace?</h2>
  <div class="divider"></div>
  <div class="step" style="left:86px">
    <svg class="step-marker" width="60" height="134" viewBox="0 0 60 134"><path d="M0 0h22l28 67-28 67H0l28-67Z" fill="var(--ink)"/><circle cx="30" cy="67" r="16" fill="var(--white)"/><text x="30" y="73" text-anchor="middle" font-family="Raleway,sans-serif" font-size="17" font-weight="700" fill="var(--orange)">1</text></svg>
    <h3>Once login</h3>
    <p style="top:64px">Upload financial statements. Select preferences. Finish the registration.</p>
  </div>
  <div class="step" style="left:468px">
    <svg class="step-marker" width="60" height="134" viewBox="0 0 60 134"><path d="M0 0h22l28 67-28 67H0l28-67Z" fill="var(--ink)"/><circle cx="30" cy="67" r="16" fill="var(--white)"/><text x="30" y="73" text-anchor="middle" font-family="Raleway,sans-serif" font-size="17" font-weight="700" fill="var(--orange)">2</text></svg>
    <h3>Automatic</h3>
    <p style="top:64px">Fare change We pick the cheapest fare for you and carry out the change automatically.</p>
  </div>
  <div class="step" style="left:850px">
    <svg class="step-marker" width="60" height="134" viewBox="0 0 60 134"><path d="M0 0h22l28 67-28 67H0l28-67Z" fill="var(--ink)"/><circle cx="30" cy="67" r="16" fill="var(--white)"/><text x="30" y="73" text-anchor="middle" font-family="Raleway,sans-serif" font-size="17" font-weight="700" fill="var(--orange)">3</text></svg>
    <h3>Sit back and save money</h3>
    <p style="top:90px">Upload financial statements. Select preferences. Finish the registration.</p>
  </div>
  <a class="btn" href="#">Register Now</a>
</section>

<footer class="site-footer">
  <div class="brand">Energy Ace<span class="brand-dot"></span></div>
  <nav class="footer-nav">
    <a href="#">That's How It Works</a><span>|</span><a href="#">Prices</a><span>|</span><a href="#">Ask?</a><span>|</span><a href="#">About Us</a><span>|</span><a href="#">Operations</a><span>|</span><a href="#">Experience</a><span>|</span><a href="#">Press</a>
  </nav>
  <p class="copyright">© Copyright 2019. All Rights Reserved.</p>
  <a class="social" href="#" aria-label="Social profile"></a>
</footer>

</body>
</html>
```